Business Card Design

I'm a commercial general contractor remodel offices, hotels, health clubs and stores mostly San Francisco and the peninsula
the file I down loaded is kind of what I want I like the I beam with my company name in it, that would be fine with me but if you have better Idea will look at it you never know, I'm decided to give in and change my company name to how every one knows me, I have been in business since 1991, I like the I beam logo I included one of my old card from my old company for reference for you.

Industry/Entity Type

Business

Contact Information for Business Card

BRAVO CONSTRUCTION (is my company name)
Reginald Pottle contractor, LIc 384217
4318 Quarry Lane, San Bruno, California 94066
mobile, (415) 555-0147
phone (650) 555-0183
Fax, (650) 555-0184
email, bravo@bravoconstruction.example

```html
<!DOCTYPE html>
<html lang="en">
<head>
<meta charset="utf-8">
<title>Bravo Construction – Business Card</title>
<link rel="stylesheet" href="https://fonts.googleapis.com/css2?family=Hind:wght@400;500;600&family=Josefin+Sans:wght@600&display=swap">
<style>
  :root {
    --backdrop: #e9e6e1;
    --card-white: #ffffff;
    --navy: #0f2236;
    --accent-blue: #1f7fd0;
    --name-blue: #2f8fe0;
    --title-ink: #1b2a3a;
    --logo-blue: #3a6fb3;
    --text-light: #ffffff;
  }
  * { box-sizing: border-box; margin: 0; padding: 0; }
  html, body {
    width: 1200px; height: 900px; overflow: hidden;
    background: var(--backdrop);
  }
  .canvas { position: relative; width: 1200px; height: 900px; }
  .business-card {
    position: absolute; left: 100px; top: 165px;
    width: 1000px; height: 571px;
    background: var(--card-white);
    box-shadow: 0 14px 40px rgba(0,0,0,0.18);
    overflow: hidden;
    font-family: "Hind", sans-serif;
  }
  .card-waves { position: absolute; inset: 0; }
  .company-title {
    position: absolute; top: 40px; left: 0; right: 0;
    text-align: center;
    font-family: "Josefin Sans", sans-serif;
    font-weight: 600; font-size: 54px; letter-spacing: 5px;
    color: var(--title-ink);
  }
  .brand-mark {
    position: absolute; top: 132px; left: 0; right: 0;
    display: flex; justify-content: center; align-items: center; gap: 12px;
  }
  .brand-square { width: 30px; height: 30px; background: var(--logo-blue); }
  .brand-name {
    font-family: "Hind", sans-serif; font-weight: 600;
    font-size: 40px; line-height: 1.2; color: var(--logo-blue); letter-spacing: 1px;
  }
  .contact-block {
    position: absolute; right: 48px; top: 262px;
    text-align: right; color: var(--text-light);
  }
  .person-name {
    font-size: 34px; font-weight: 500; letter-spacing: 1px;
    color: var(--text-light); line-height: 1.1;
  }
  .person-role { font-size: 18px; line-height: 1.3; }
  .license { font-size: 22px; color: var(--name-blue); font-weight: 500; margin-top: 4px; }
  .phone-line { font-size: 22px; line-height: 1.5; }
  .address-line {
    position: absolute; right: 48px; top: 490px;
    font-size: 21px; color: var(--text-light);
  }
  .office-block {
    position: absolute; left: 48px; top: 452px;
    font-size: 21px; color: var(--text-light); line-height: 1.55;
  }
</style>
</head>
<body>
<main class="canvas">
  <section class="business-card">
    <svg class="card-waves" width="1000" height="571" viewBox="0 0 1000 571" aria-hidden="true">
      <path d="M0,396 C250,390 420,220 1000,165 L1000,200 C420,240 250,410 0,420 Z" fill="var(--accent-blue)"/>
      <path d="M0,418 C250,408 420,238 1000,198 L1000,571 L0,571 Z" fill="var(--navy)"/>
    </svg>

    <h1 class="company-title">BRAVO CONSTRUCTION</h1>

    <div class="brand-mark">
      <span class="brand-square"></span>
      <span class="brand-name">BRAVO BUILD</span>
    </div>

    <div class="contact-block">
      <p class="person-name">REGINALD POTTLE</p>
      <p class="person-role">Contractor</p>
      <p class="license">Lic #384217</p>
      <p class="phone-line">Cell : (415) 555-0147</p>
      <p class="phone-line">Telephone : (650) 555-0183</p>
    </div>

    <p class="address-line">Address : 4318 Quarry Lane San Bruno, Ca 94066</p>

    <div class="office-block">
      <p>Fax : (650) 555-0184</p>
      <p>Email : bravo@bravoconstruction.example</p>
      <p>www.bravoconstruction.example</p>
    </div>
  </section>
</main>
</body>
</html>
```